Online video and marketing company business cards

Need to get some new business cards designed to fit with our new logo. The cards should be professional, clean and simple.

Cards should have:

Name
Position
2 line address
telephone
mobile
email address
web address

We need to have our logo and if possible say what we do...
ONLINE FILM PRODUCTION & STRATEGY

Marketing

```html
<!DOCTYPE html>
<html lang="en">
<head>
<meta charset="utf-8">
<title>Streamvale business cards</title>
<link rel="stylesheet" href="https://fonts.googleapis.com/css2?family=Dosis:wght@500;600;700&display=swap">
<style>
  :root {
    --backdrop: #e6e6e6;
    --card: #ffffff;
    --brand-dark: #1f5a8c;
    --brand-light: #6aaecb;
    --ink: #1d4f7a;
    --muted: #c6c6c6;
    --icon: #ffffff;
  }
  * { margin: 0; padding: 0; box-sizing: border-box; }
  html, body { width: 1200px; height: 947px; overflow: hidden; }
  body {
    background: var(--backdrop);
    font-family: "Dosis", sans-serif;
    position: relative;
  }
  .card {
    position: absolute;
    width: 520px;
    height: 300px;
    background: var(--card);
    box-shadow: 0 6px 18px rgba(0,0,0,0.12);
  }
  .card-front { left: 620px; top: 110px; }
  .card-back { left: 60px; top: 500px; }

  /* front */
  .front-brand {
    position: absolute;
    left: 0; right: 0; top: 108px;
    text-align: center;
  }
  .brand-name {
    font-weight: 700;
    font-size: 54px;
    color: var(--brand-dark);
    letter-spacing: 0.5px;
    line-height: 1;
    display: inline-flex;
    align-items: center;
    gap: 10px;
  }
  .brand-dot {
    width: 26px; height: 26px;
    border-radius: 50%;
    background: var(--brand-light);
    display: inline-block;
  }
  .front-web {
    margin-top: 8px;
    font-size: 17px;
    font-weight: 600;
    color: var(--brand-light);
    letter-spacing: 0.4px;
  }

  /* back */
  .icon-strip {
    position: absolute;
    left: 0; top: 38px;
    width: 42px; height: 128px;
    background: var(--brand-light);
    border-radius: 0 10px 10px 0;
    display: flex;
    flex-direction: column;
    justify-content: space-around;
    align-items: center;
    padding: 8px 0;
  }
  .icon-strip svg { width: 16px; height: 16px; }
  .contact-list {
    position: absolute;
    left: 58px; top: 44px;
    color: var(--ink);
    font-weight: 600;
    font-size: 15px;
    line-height: 19px;
  }
  .contact-list p { margin-bottom: 5px; }
  .phone-row { display: flex; align-items: center; gap: 12px; }
  .mobile { display: inline-flex; align-items: center; gap: 5px; }
  .mobile svg { width: 12px; height: 16px; }
  .name-tab {
    position: absolute;
    right: 0; top: 132px;
    width: 190px; height: 30px;
    background: var(--brand-light);
    border-radius: 8px 0 0 8px;
    color: #fff;
    font-size: 19px;
    font-weight: 600;
    letter-spacing: 0.5px;
    line-height: 30px;
    padding-left: 40px;
  }
  .position {
    position: absolute;
    right: 56px; top: 166px;
    color: var(--ink);
    font-size: 14px;
    font-weight: 600;
  }
  .back-brand {
    position: absolute;
    right: 40px; bottom: 28px;
    font-size: 34px;
    font-weight: 700;
    color: var(--muted);
    display: inline-flex;
    align-items: center;
    gap: 8px;
  }
  .back-brand .brand-dot { width: 18px; height: 18px; background: var(--muted); }
</style>
</head>
<body>

<section class="card card-front">
  <div class="front-brand">
    <div class="brand-name"><span class="brand-dot"></span>streamvale</div>
    <div class="front-web">www.yourwebsite.com</div>
  </div>
</section>

<section class="card card-back">
  <div class="icon-strip">
    <svg viewBox="0 0 16 16" aria-label="Address"><path d="M8 1a5 5 0 0 0-5 5c0 4 5 9 5 9s5-5 5-9a5 5 0 0 0-5-5zm0 7a2 2 0 1 1 0-4 2 2 0 0 1 0 4z" fill="var(--icon)"/></svg>
    <svg viewBox="0 0 16 16" aria-label="Telephone"><path d="M4 1l3 3-2 2c1 2 3 4 5 5l2-2 3 3-2 3C7 15 1 9 1 3z" fill="var(--icon)"/></svg>
    <svg viewBox="0 0 16 16" aria-label="Email"><rect x="1" y="3" width="14" height="10" fill="none" stroke="var(--icon)" stroke-width="1.5"/><path d="M1 3l7 6 7-6" fill="none" stroke="var(--icon)" stroke-width="1.5"/></svg>
    <svg viewBox="0 0 16 16" aria-label="Website"><circle cx="8" cy="8" r="6.5" fill="none" stroke="var(--icon)" stroke-width="1.3"/><path d="M1.5 8h13M8 1.5c-3 3.5-3 9.5 0 13M8 1.5c3 3.5 3 9.5 0 13" fill="none" stroke="var(--icon)" stroke-width="1.1"/></svg>
  </div>

  <div class="contact-list">
    <p>Your residential or commercial or office address<br>in two line</p>
    <p class="phone-row">
      <span>[00] 00 00000</span>
      <span class="mobile">
        <svg viewBox="0 0 12 16" aria-label="Mobile"><rect x="1" y="1" width="10" height="14" rx="2" fill="var(--ink)"/><rect x="3" y="3" width="6" height="8" fill="#fff"/></svg>
        [00] 0000000000
      </span>
    </p>
    <p>info.support@yourwebsite.com</p>
    <p>www.yourwebsite.com</p>
  </div>

  <div class="name-tab">YOUR NAME</div>
  <div class="position">Position</div>

  <div class="back-brand"><span class="brand-dot"></span>streamvale</div>
</section>

</body>
</html>
```